The Harwell Selection Web Site design

I need a web design for my luxury range of Terry Toweling and Spa Accessories for luxury upmarket hotels and Spas. I have a catalog that sets the mood and tone I am looking for. I need a website design that shows off the look and feel of this luxury range while working back to the catalog look and feel. Its all about Upmarket and Luxury. I will be using the website as a reference site and as a site that customers can purchase off.
The Logo is attached as is the catalog. I don't mind changing the color of the Logo to match the website. However I would prefer to keep the font of that logo.

http://quillgallery.framevista.example/p559203417
Please can you try and access this link. The Harwell Selection
Name Trudie. Email trudie@kestrelsupply.example.au. Password Harwell.
These images are to be used for shopping page and please use the close up details of texture as background on pages and use those texture details and close ups for banners

Please note the look and feel has to be very upmarket and super luxury. Ficus is on mood and not on retail.
Have a look at the mood on the following websites
Www.velvetharbourstays.example
And oursandycovecottagestore.example
That one is retail .mi don't want retail focus but it's very clean. And simple and colors are good
Updates

Please rebook brief. I have added some important detail. Thanks

Relook brief. I have added,important detail. Thanks

Target Market(s)

Corporate buyers
This is not for retail selling to consumers
Price it's viewed only after secure login

Industry/Entity Type

Shopping

Colors
acd037
cadf82
fbc995
fce7d3
faa54b

Requirements
Must have
• Luxury. Think luxury. Very high end yet modern like the catalogue
Use banners on home page
Should not have
• Don't use the blue as the main color. It's too cheap.
No products on home page

```html
<!DOCTYPE html>
<html lang="en">
<head>
<meta charset="utf-8">
<title>The Harwell Selection</title>
<link href="https://fonts.googleapis.com/css2?family=Lobster&family=Libre+Baskerville&family=Open+Sans:ital,wght@0,400;0,600;1,400&family=Arimo:wght@400;700&display=swap" rel="stylesheet">
<style>
:root{
  --orange:#faa54b;
  --orange-deep:#e87d0a;
  --orange-text:#f39a3c;
  --green:#acd037;
  --black:#000;
  --tile-dark:#333;
  --white:#fff;
  --grey-text:#bbb;
  --client-grey:#a8a8a8;
  --body-text:#222;
  --red:#c8141a;
}
*{margin:0;padding:0;box-sizing:border-box}
html,body{width:986px;height:1200px;overflow:hidden;background:var(--black)}
body{position:relative;font-family:Arimo,Arial,sans-serif}
.abs{position:absolute}
.topbar{left:0;top:0;width:986px;height:28px;background:var(--orange)}
.dot{position:absolute;border-radius:50%}
.topbar .dot{width:20px;height:20px;top:4px;background:#222}
.account-links{position:absolute;left:749px;top:8px;font-size:10px;color:#222;white-space:nowrap}
.account-links span{margin-right:9px}
.header{left:0;top:28px;width:986px;height:109px;background:var(--black)}
.logo{left:146px;top:49px;font-family:Lobster,cursive;font-size:37px;line-height:44px;color:var(--orange-text);white-space:nowrap}
.search{left:577px;top:59px;width:122px;height:24px;background:var(--white);font-size:11px;font-style:italic;color:#333;padding:6px 0 0 13px}
.search-btn{left:555px;top:59px;width:25px;height:24px;border-radius:50%;background:var(--orange)}
.call{left:742px;top:56px;color:var(--white);white-space:nowrap}
.call small{display:block;font-size:12px}
.call strong{display:block;font-size:16px;font-weight:400}
.nav{top:111px;font-family:"Libre Baskerville",serif;font-size:12.5px;color:var(--white);white-space:nowrap}
.nav-active{left:145px;top:128px;width:39px;height:2px;background:var(--green)}
.hero{left:0;top:137px;width:986px;height:291px;background:linear-gradient(100deg,#5d5a55 0%,#7d8388 25%,#b0a89c 45%,#6e5b4b 70%,#4a3d33 100%)}
.hero-caption{left:193px;top:262px;width:597px;height:56px;background:rgba(120,115,110,.55);font-family:"Libre Baskerville",serif;font-size:21px;line-height:25px;color:var(--white);text-align:center;padding-top:2px;white-space:nowrap}
.hero-arrow{width:34px;height:34px;top:265px;border-radius:50%;background:#f2f2f2}
.tile{position:absolute;width:161px;height:134px}
.tile-text{padding:13px 0 0 15px;color:var(--white)}
.tile-text h3{font-family:Lobster,cursive;font-weight:400;font-size:22px;line-height:28px;margin-bottom:10px;white-space:nowrap}
.tile-text p{font-size:11px;line-height:14px;width:172px}
.tile svg{position:absolute;right:16px;bottom:15px}
.info{left:0;top:757px;width:986px;height:188px;background:var(--white)}
.info h2{font-family:"Open Sans",sans-serif;font-weight:400;font-size:15.5px;color:var(--orange-text);position:absolute;white-space:nowrap}
.info p{position:absolute;font-size:10.5px;line-height:14px;color:var(--body-text)}
.btn-more{left:145px;top:134px;width:67px;height:18px;background:var(--green);color:var(--white);font-family:"Open Sans",sans-serif;font-size:10.5px;font-weight:600;text-align:center;line-height:18px}
.pdf-bar{left:410px;top:112px;width:186px;height:35px;border-radius:6px;background:linear-gradient(#e1242a,var(--red));color:var(--white);font-size:17px;font-weight:700;line-height:35px;padding-left:30px;white-space:nowrap}
.product{left:616px;top:33px;width:225px;height:119px;background:#ccc;padding:3px}
.product-photo{width:219px;height:113px;background:linear-gradient(#6e4e2a,#a58b6a 55%,#e6e3dd);position:relative}
.product-caption{position:absolute;left:0;bottom:0;width:219px;height:20px;background:var(--green);color:var(--white);font-size:12.5px;font-weight:700;text-align:center;line-height:20px;white-space:nowrap}
.clients-title{left:146px;top:984px;font-family:"Open Sans",sans-serif;font-style:italic;font-size:15px;color:var(--orange-text);white-space:nowrap}
.client{top:984px;text-align:center;color:var(--client-grey);font-family:Arimo,Arial,sans-serif;font-size:15px;line-height:20px;white-space:nowrap}
.footer-rule{left:0;top:1040px;width:986px;height:1px;background:#555}
.fcol{top:1048px;color:var(--grey-text);font-size:9.5px;line-height:13.2px;white-space:nowrap}
.fcol h4{color:var(--white);font-size:11.5px;margin-bottom:5px}
.email-field{left:373px;top:1105px;width:115px;height:18px;background:var(--white);border:1px solid var(--green);font-size:9px;font-style:italic;color:#333;padding:3px 4px}
.submit{left:373px;top:1134px;width:59px;height:18px;background:var(--green);color:var(--white);font-size:10.5px;font-weight:700;text-align:center;line-height:18px}
.contact dt{float:left;clear:left;width:15px;color:var(--white);font-weight:700}
.contact dd{margin-left:15px;margin-bottom:9px}
.pay-badge{left:731px;top:1096px;width:102px;height:64px;background:var(--white)}
.bottombar{left:0;top:1178px;width:986px;height:22px;background:var(--orange)}
.copyright{left:146px;top:5px;font-size:9.5px;color:#222;white-space:nowrap}
.foot-logo{left:714px;top:1px;font-family:Lobster,cursive;font-size:15px;color:#111;white-space:nowrap}
</style>
</head>
<body>

<div class="abs topbar">
  <span class="dot" style="left:146px"></span>
  <span class="dot" style="left:169px"></span>
  <span class="dot" style="left:193px"></span>
  <span class="dot" style="left:216px"></span>
  <span class="dot" style="left:239px"></span>
  <svg class="abs" style="left:713px;top:4px" width="20" height="20" viewBox="0 0 20 20" aria-label="Cart">
    <circle cx="10" cy="10" r="10" fill="#222"/>
    <path d="M5 6h2l1.5 6h6l1.2-4.5H8" stroke="#faa54b" stroke-width="1.4" fill="none"/>
    <circle cx="9" cy="14.5" r="1" fill="#faa54b"/><circle cx="14" cy="14.5" r="1" fill="#faa54b"/>
  </svg>
  <div class="account-links"><span>Registration</span>Log In</div>
</div>

<header class="abs header"></header>
<div class="abs logo">The Harwell Selection</div>
<div class="abs search-btn"></div>
<svg class="abs" style="left:561px;top:65px" width="13" height="13" viewBox="0 0 13 13"><circle cx="5.5" cy="5.5" r="3.6" stroke="#fff" stroke-width="1.8" fill="none"/><path d="M8 8l3.5 3.5" stroke="#fff" stroke-width="2"/></svg>
<div class="abs search">Search here</div>
<svg class="abs" style="left:712px;top:57px" width="26" height="26" viewBox="0 0 26 26" aria-label="Phone">
  <circle cx="13" cy="13" r="12" stroke="#fff" stroke-width="1.5" fill="none"/>
  <path d="M10 7c-2 1-2 4 0 7s4 5 6 5l1.5-2-2.5-2-1.2 1c-1-.6-2.4-2.4-2.8-3.4l1.1-1L11 7z" fill="#fff"/>
</svg>
<div class="abs call"><small>Call Us Today</small><strong>123 456 7890</strong></div>

<nav>
  <span class="abs nav" style="left:146px">Home</span>
  <span class="abs nav" style="left:244px">About Us</span>
  <span class="abs nav" style="left:359px">Products</span>
  <span class="abs nav" style="left:473px">New Collection</span>
  <span class="abs nav" style="left:623px">Accessories</span>
  <span class="abs nav" style="left:752px">Contact Us</span>
</nav>
<div class="abs nav-active"></div>

<div class="abs hero" role="img" aria-label="Spa room with a freestanding bath, candles and towel-draped treatment beds"></div>
<div class="abs hero-caption">We Allows You To TransformYour Bathroom, Spa, Or<br>Poolside Into A True Retreat.</div>
<div class="abs hero-arrow" style="left:145px"></div>
<svg class="abs" style="left:156px;top:276px" width="12" height="12" viewBox="0 0 12 12"><path d="M8 1L3 6l5 5" stroke="#444" stroke-width="2" fill="none"/></svg>
<div class="abs hero-arrow" style="left:806px"></div>
<svg class="abs" style="left:817px;top:276px" width="12" height="12" viewBox="0 0 12 12"><path d="M4 1l5 5-5 5" stroke="#444" stroke-width="2" fill="none"/></svg>

<section>
  <div class="tile" style="left:145px;top:460px;background:linear-gradient(#2b3a2a,#6d7f86 55%,#e8e8e6)" role="img" aria-label="Massage table draped in white by the waterside"></div>
  <div class="tile" style="left:306px;top:460px;width:187px;background:var(--green)">
    <div class="tile-text"><h3>Spa Accessories</h3><p>Lorem ipsum dolor sit amet consectetuer adipiscing elit sed diam nonummy nibh euismod</p></div>
    <svg width="22" height="22" viewBox="0 0 22 22"><circle cx="11" cy="11" r="10" stroke="#fff" stroke-width="1.5" fill="none"/><path d="M9 6l5 5-5 5" stroke="#fff" stroke-width="1.6" fill="none"/></svg>
  </div>
  <div class="tile" style="left:493px;top:460px;width:162px;background:linear-gradient(160deg,#3e4a33,#3a3f55 50%,#6a6660)" role="img" aria-label="Folded textured throws in green, navy and grey"></div>
  <div class="tile" style="left:655px;top:460px;width:186px;background:var(--tile-dark)">
    <div class="tile-text"><h3>New Collection</h3><p>Lorem ipsum dolor sit amet consectetuer adipiscing elit sed diam nonummy nibh euismod</p></div>
    <svg width="22" height="22" viewBox="0 0 22 22"><circle cx="11" cy="11" r="10" stroke="#fff" stroke-width="1.5" fill="none"/><path d="M9 6l5 5-5 5" stroke="#fff" stroke-width="1.6" fill="none"/></svg>
  </div>
  <div class="tile" style="left:145px;top:594px;width:187px;background:var(--tile-dark)">
    <div class="tile-text"><h3>Terry Towels</h3><p>Lorem ipsum dolor sit amet consectetuer adipiscing elit sed diam nonummy nibh euismod</p></div>
    <svg width="22" height="22" viewBox="0 0 22 22"><circle cx="11" cy="11" r="10" stroke="#fff" stroke-width="1.5" fill="none"/><path d="M9 6l5 5-5 5" stroke="#fff" stroke-width="1.6" fill="none"/></svg>
  </div>
  <div class="tile" style="left:332px;top:594px;background:linear-gradient(#e2492b,#2c3441 35%,#ea7a2a 60%,#e24a28)" role="img" aria-label="Stack of colourful terry towels"></div>
  <div class="tile" style="left:493px;top:594px;width:187px;background:var(--orange-deep)">
    <div class="tile-text"><h3>Throws</h3><p>Lorem ipsum dolor sit amet consectetuer adipiscing elit sed diam nonummy nibh euismod</p></div>
    <svg width="22" height="22" viewBox="0 0 22 22"><circle cx="11" cy="11" r="10" stroke="#fff" stroke-width="1.5" fill="none"/><path d="M9 6l5 5-5 5" stroke="#fff" stroke-width="1.6" fill="none"/></svg>
  </div>
  <div class="tile" style="left:680px;top:594px;background:linear-gradient(135deg,#d8d6d2,#9fb9b6 45%,#c23a36 70%,#e5e3df)" role="img" aria-label="Striped throws hanging over a rail"></div>
</section>

<section class="abs info">
  <h2 style="left:145px;top:29px">About Us</h2>
  <p style="left:145px;top:58px;width:200px">Lorem ipsum dolor sit amet, consectetuer adipiscing elit, sed diam nonummy nreibh euismod tincidunt ut laoreet dolore magna aliquam erat volutpat. Ut wisi enim ad min veniam, quis nostrud exerci tation ullam</p>
  <div class="abs btn-more">Read More</div>
  <h2 style="left:383px;top:29px">Download Our Brochure</h2>
  <p style="left:387px;top:58px;width:200px">Lorem ipsum dolor sit amet, consectetuer adipiscing elit sed diam non</p>
  <div class="abs pdf-bar">Download PDF</div>
  <svg class="abs" style="left:385px;top:102px" width="36" height="50" viewBox="0 0 36 50" aria-label="PDF document">
    <path d="M1 1h24l10 10v38H1z" fill="#fff" stroke="#999"/>
    <path d="M25 1v10h10" fill="#eee" stroke="#999"/>
    <rect x="1" y="8" width="22" height="10" fill="#d2232a"/>
    <text x="4" y="16" font-family="Arimo,sans-serif" font-size="8" font-weight="700" fill="#fff">PDF</text>
  </svg>
  <div class="abs product">
    <div class="product-photo" role="img" aria-label="Stack of folded white towels">
      <div class="product-caption">Our Newly Launched Product</div>
    </div>
  </div>
</section>

<div class="abs clients-title">Some of&nbsp; Our Clients</div>
<div class="abs client" style="left:322px;width:90px">Corvane</div>
<div class="abs client" style="left:452px;width:105px">Belmaris</div>
<div class="abs client" style="left:598px;width:82px">Ninefold</div>
<div class="abs client" style="left:735px;width:110px">Ashford Lyle</div>

<div class="abs footer-rule"></div>
<div class="abs fcol" style="left:147px"><h4>Quick Links</h4>Home<br>About Us<br>Products<br>New Collection<br>Accessories<br>Contact Us</div>
<div class="abs fcol" style="left:249px"><h4>Service &amp; Support</h4>My Account<br>Terms &amp; Conditions<br>Buying Guide<br>Shipping Details<br>FAQ's<br>My Cart<br>Terms of Use</div>
<div class="abs fcol" style="left:373px"><h4>Newsletter SignUp</h4>Join Our newsletter list<br>to get the latest updates</div>
<div class="abs email-field">email address</div>
<div class="abs submit">Submit</div>
<div class="abs fcol" style="left:521px"><h4>Contact Information</h4>
  <dl class="contact">
    <dt>A:</dt><dd>Street Name, City Name<br>State Zip Code</dd>
    <dt>P:</dt><dd>123-456-7890</dd>
    <dt>F:</dt><dd>456-789-4504</dd>
    <dt>E:</dt><dd>Support@harwellselection.example</dd>
  </dl>
</div>
<div class="abs fcol" style="left:720px"><h4>Follow Us On</h4></div>
<span class="dot" style="left:719px;top:1068px;width:19px;height:19px;background:var(--green)"></span>
<span class="dot" style="left:742px;top:1068px;width:19px;height:19px;background:var(--orange)"></span>
<span class="dot" style="left:766px;top:1068px;width:19px;height:19px;background:var(--orange)"></span>
<span class="dot" style="left:790px;top:1068px;width:19px;height:19px;background:var(--orange)"></span>
<span class="dot" style="left:814px;top:1068px;width:19px;height:19px;background:var(--orange)"></span>
<div class="abs pay-badge" role="img" aria-label="Accepted payment methods"></div>

<div class="abs bottombar">
  <div class="abs copyright">©2014&nbsp; TheHarwellSelection&nbsp; All Rights Reserved</div>
  <div class="abs foot-logo">The Harwell Selection</div>
</div>

</body>
</html>
```